Wine Company Flyer Design

Hello,

I need a flyer design that will fit an 11 inch width by 17 inch height. Design has to be submitted in PDF X-1a format.

We want our logo on the flyer with the slogan underneath it saying "Better Wines Lower Prices"

We want a nice design and then we will get to some of the text that will be on the flyer.

Please make the flyer in two colors ONLY. Use the colors of our logo for the rest of the design.

Requirements
Must have
• PDF x-1a format
• Logo on flyer with slogan "Better Wines Lower Prices" underneath
• Two colors - Orange, Red (Same as logo colors)
• Fits in an 11"x17" format for printing
• This will be for the wine industry so include elements of wine in the flyer and make it look nice. Leave some space in the middle of the design for text to be put in.

```html
<!DOCTYPE html>
<html lang="en">
<head>
<meta charset="utf-8">
<title>VinoValue Flyer</title>
<link rel="stylesheet" href="https://fonts.googleapis.com/css2?family=Oswald:wght@500;600&family=Roboto+Condensed:wght@700&family=Mulish:wght@400&display=swap">
<style>
  :root {
    --red: #e3171e;
    --orange: #f29300;
    --backdrop: #5b5b5d;
    --paper: #ffffff;
  }
  * { margin: 0; padding: 0; box-sizing: border-box; }
  html, body { width: 1200px; height: 1200px; overflow: hidden; background: var(--backdrop); }
  .flyer {
    position: absolute; left: 257px; top: 69px; width: 687px; height: 1063px;
    background: var(--paper); overflow: hidden;
  }
  .brand-name {
    position: absolute; top: 118px; left: 0; width: 100%; text-align: center;
    font-family: "Oswald", sans-serif; font-weight: 600; font-size: 56px;
    letter-spacing: -1px; color: var(--red); line-height: 1;
  }
  .brand-dot {
    position: absolute; top: 38px; left: 293px; width: 100px; height: 100px;
    border-radius: 50%; background: var(--orange);
  }
  .slogan {
    position: absolute; top: 228px; left: 0; width: 100%;
    display: flex; justify-content: center; align-items: center; gap: 12px;
    font-family: "Mulish", sans-serif; font-weight: 400; font-size: 25px;
    letter-spacing: 1px; color: var(--orange);
  }
  .slogan .glass { width: 34px; height: 58px; }
  .features { position: absolute; top: 312px; left: 0; width: 100%; list-style: none; }
  .feature {
    position: relative; text-align: center;
    font-family: "Roboto Condensed", sans-serif; font-weight: 700; font-size: 24px;
    letter-spacing: 1px; line-height: 30px; color: var(--red); text-transform: uppercase;
    margin-bottom: 30px;
  }
  .feature .glass { position: absolute; width: 20px; height: 38px; top: -8px; }
  .feature .code { color: var(--orange); }
  .contact {
    position: absolute; top: 656px; left: 0; width: 100%; text-align: center;
    font-family: "Mulish", sans-serif; font-size: 16px; line-height: 27px; color: var(--red);
  }
  .contact .icon { display: inline-block; width: 10px; height: 10px; vertical-align: 0; margin-right: 4px; }
  .bottle-band {
    position: absolute; left: 0; bottom: 0; width: 100%; height: 320px;
    background: linear-gradient(90deg, var(--red) 0%, var(--orange) 14%, var(--red) 28%, var(--orange) 42%, var(--red) 54%, var(--orange) 64%, var(--red) 76%, var(--orange) 88%, var(--red) 100%);
  }
</style>
</head>
<body>
<main class="flyer">
  <div class="brand-dot"></div>
  <h1 class="brand-name">VINOVALUE</h1>

  <p class="slogan">
    <span>Better Wines</span>
    <svg class="glass" viewBox="0 0 34 58" aria-hidden="true">
      <path d="M8 2 L30 6 Q31 22 20 30 Q10 30 6 20 Z" fill="none" stroke="var(--red)" stroke-width="2"/>
      <path d="M7 16 Q18 20 30 14 Q28 28 19 29 Q10 28 7 16 Z" fill="var(--red)"/>
      <path d="M18 30 L12 54 M4 55 L22 52" stroke="var(--red)" stroke-width="2.5" fill="none"/>
    </svg>
    <span>Lower Prices</span>
  </p>

  <ul class="features">
    <li class="feature">
      <svg class="glass" style="left:82px" viewBox="0 0 20 38" aria-hidden="true"><path d="M2 1 H18 Q19 15 10 17 Q1 15 2 1 Z" fill="none" stroke="var(--red)" stroke-width="1.6"/><path d="M2 7 H18 Q18 15 10 16 Q2 15 2 7 Z" fill="var(--red)"/><path d="M10 17 V35 M4 36 H16" stroke="var(--red)" stroke-width="2"/></svg>
      <span style="padding-left:30px">100's of popular and collector wines</span><br>in stock.
    </li>
    <li class="feature">
      <svg class="glass" style="left:105px" viewBox="0 0 20 38" aria-hidden="true"><path d="M2 1 H18 Q19 15 10 17 Q1 15 2 1 Z" fill="none" stroke="var(--red)" stroke-width="1.6"/><path d="M2 7 H18 Q18 15 10 16 Q2 15 2 7 Z" fill="var(--red)"/><path d="M10 17 V35 M4 36 H16" stroke="var(--red)" stroke-width="2"/></svg>
      <span style="padding-left:30px">Free shipping on 6 packs or more.</span><br>
      <span style="padding-left:30px">Use code <span class="code">"SHIPFREE1"</span> at checkout.</span>
    </li>
    <li class="feature">
      <svg class="glass" style="left:125px" viewBox="0 0 20 38" aria-hidden="true"><path d="M2 1 H18 Q19 15 10 17 Q1 15 2 1 Z" fill="none" stroke="var(--red)" stroke-width="1.6"/><path d="M2 7 H18 Q18 15 10 16 Q2 15 2 7 Z" fill="var(--red)"/><path d="M10 17 V35 M4 36 H16" stroke="var(--red)" stroke-width="2"/></svg>
      <span style="padding-left:28px">Mix and match 1 to 18 bottles</span><br>for yourself or as a gift.
    </li>
    <li class="feature">
      <svg class="glass" style="left:125px" viewBox="0 0 20 38" aria-hidden="true"><path d="M2 1 H18 Q19 15 10 17 Q1 15 2 1 Z" fill="none" stroke="var(--red)" stroke-width="1.6"/><path d="M2 7 H18 Q18 15 10 16 Q2 15 2 7 Z" fill="var(--red)"/><path d="M10 17 V35 M4 36 H16" stroke="var(--red)" stroke-width="2"/></svg>
      <span style="padding-left:28px">Custom gift letters available.</span>
    </li>
  </ul>

  <div class="contact">
    <div><svg class="icon" viewBox="0 0 10 10" aria-hidden="true"><circle cx="5" cy="5" r="4.2" fill="none" stroke="var(--red)" stroke-width="1.2"/><path d="M1 5 H9 M5 1 V9" stroke="var(--red)" stroke-width="1"/></svg>vinovalue.com</div>
    <div><svg class="icon" viewBox="0 0 10 10" aria-hidden="true"><rect x="0.5" y="2" width="9" height="6.5" fill="var(--red)"/><path d="M0.5 2 L5 6 L9.5 2" stroke="#fff" stroke-width="1" fill="none"/></svg>customerservice@vinovalue.com</div>
  </div>

  <div class="bottle-band" role="img" aria-label="Row of overlapping red and orange wine bottle silhouettes along the bottom edge"></div>
</main>
</body>
</html>
```